No Credit Score QT and ZMR

I'm looking for a banner to display on emails as well as facebook. The facebook banner would need to be square and the other size is 728 x 90. We are a mortgage company that does mostly Military home loans. We would like to start out with just this banner, then do about 20 others once we find the right designer. I need something simple but that stands out. Our company website is www.harborpeakfinancial.com. The text for this will be ( Ask about our "No Credit Score" program for ZMR and QT)

```html
<!DOCTYPE html>
<html lang="en">
<head>
<meta charset="utf-8">
<title>Military home loans – Harbor Peak Financial</title>
<link href="https://fonts.googleapis.com/css2?family=Montserrat:wght@300;400;700;800&family=Arimo:wght@400;700&display=swap" rel="stylesheet">
<style>
  :root {
    --brand-blue: #3c6eb6;
    --deep-blue: #2f5aa8;
    --panel-blue: #4a79c6;
    --light-blue: #8fb3e4;
    --pale-blue: #dfe8f5;
    --cyan: #2ab4e6;
    --yellow: #f6e51b;
    --red: #e52421;
    --green: #8cc63f;
    --text-dark: #333333;
    --text-url: #3a4f7a;
    --grey-bg: #eceef1;
    --white: #ffffff;
  }
  html, body {
    margin: 0;
    padding: 0;
    overflow: hidden;
    background: var(--white);
  }
  .banner {
    position: relative;
    width: 1200px;
    height: 151px;
    overflow: hidden;
    background: var(--white);
    font-family: "Montserrat", sans-serif;
  }
  .banner-shapes {
    position: absolute;
    inset: 0;
  }
  .family-photo {
    position: absolute;
    left: 0;
    top: 0;
    width: 200px;
    height: 151px;
    background: linear-gradient(180deg, #cdd6dc 0%, #b9b5a8 55%, #7d8f5a 100%);
  }
  .corner-ribbon {
    position: absolute;
    left: -34px;
    top: 18px;
    width: 130px;
    height: 22px;
    background: var(--red);
    color: var(--white);
    transform: rotate(-45deg);
    display: flex;
    align-items: center;
    justify-content: center;
    gap: 4px;
    font-family: "Arimo", sans-serif;
    font-size: 6px;
    font-weight: 700;
    line-height: 1;
  }
  .corner-ribbon .rate {
    font-size: 10px;
  }
  .headline {
    position: absolute;
    left: 284px;
    top: 12px;
    margin: 0;
    font-size: 45px;
    line-height: 1;
    color: var(--brand-blue);
    letter-spacing: -0.5px;
    white-space: nowrap;
  }
  .headline .strong { font-weight: 700; }
  .headline .light { font-weight: 400; }
  .program {
    position: absolute;
    left: 364px;
    top: 60px;
    margin: 0;
    font-family: "Arimo", sans-serif;
    font-size: 22px;
    color: var(--text-dark);
    white-space: nowrap;
  }
  .website {
    position: absolute;
    left: 374px;
    top: 104px;
    display: flex;
    align-items: center;
    gap: 17px;
    font-family: "Arimo", sans-serif;
    font-size: 15px;
    color: var(--text-url);
    text-decoration: none;
  }
  .website svg { display: block; }
  .offer-text {
    position: absolute;
    color: var(--white);
    font-weight: 700;
    white-space: nowrap;
    line-height: 1;
  }
  .offer-supreme {
    left: 784px;
    top: 20px;
    color: var(--red);
    font-size: 11px;
    font-weight: 800;
    line-height: 1.25;
    transform: rotate(-4deg);
  }
  .offer-think {
    left: 852px;
    top: 31px;
    font-size: 12px;
    transform: rotate(4deg);
  }
  .offer-think .small { font-size: 9px; font-weight: 400; }
  .offer-start {
    left: 786px;
    top: 76px;
    color: var(--yellow);
    font-size: 15px;
    transform: rotate(4deg);
  }
  .no-credit {
    position: absolute;
    left: 1016px;
    top: 40px;
    margin: 0;
    color: var(--white);
    line-height: 1.15;
    white-space: nowrap;
  }
  .no-credit .line-1 { display: block; font-size: 26px; font-weight: 700; }
  .no-credit .line-2 { display: block; font-size: 24px; font-weight: 300; padding-left: 4px; }
</style>
</head>
<body>
<div class="banner">
  <svg class="banner-shapes" width="1200" height="151" viewBox="0 0 1200 151" aria-hidden="true">
    <!-- right grey backdrop -->
    <polygon points="770,151 900,0 1200,0 1200,151" fill="var(--grey-bg)"/>
    <polygon points="880,151 960,60 1010,151" fill="#f6f7f9"/>
    <!-- blue panel with arrow point -->
    <polygon points="1005,0 1200,0 1200,151 1005,151 958,76" fill="var(--panel-blue)"/>
    <polygon points="1080,0 1200,0 1200,151 1150,151" fill="#5585cf" opacity="0.6"/>
    <polyline points="1010,8 966,76 1010,144" fill="none" stroke="var(--white)" stroke-width="3"/>
    <polyline points="1010,8 1200,8" fill="none" stroke="var(--white)" stroke-width="2" opacity="0.7"/>
    <!-- chevrons after photo -->
    <polygon points="196,0 212,0 258,76 212,151 196,151 242,76" fill="var(--deep-blue)"/>
    <polygon points="222,0 232,0 278,76 232,151 222,151 268,76" fill="var(--light-blue)"/>
    <polygon points="244,0 252,0 298,76 252,151 244,151 290,76" fill="var(--pale-blue)"/>
    <!-- offer ribbon -->
    <polygon points="1000,108 1020,136 1040,112" fill="var(--green)"/>
    <polygon points="766,18 960,36 958,110 764,96" fill="var(--cyan)"/>
    <polygon points="778,12 842,8 846,60 782,64" fill="var(--yellow)"/>
  </svg>

  <div class="family-photo" role="img" aria-label="Photo of a military family standing in front of their house"></div>
  <div class="corner-ribbon"><span>Military home loans</span><span class="rate">25%</span></div>

  <h1 class="headline"><span class="strong">Military home</span> <span class="light">loans.</span></h1>
  <p class="program">Program For ZMR and QT</p>

  <a class="website" href="#">
    <svg width="32" height="32" viewBox="0 0 32 32" aria-hidden="true">
      <circle cx="16" cy="16" r="16" fill="var(--brand-blue)"/>
      <g fill="none" stroke="var(--white)" stroke-width="1.4">
        <circle cx="16" cy="16" r="9"/>
        <ellipse cx="16" cy="16" rx="4" ry="9"/>
        <line x1="7" y1="16" x2="25" y2="16"/>
        <line x1="16" y1="7" x2="16" y2="25"/>
        <line x1="8.5" y1="11.5" x2="23.5" y2="11.5"/>
        <line x1="8.5" y1="20.5" x2="23.5" y2="20.5"/>
      </g>
    </svg>
    <span>www.harborpeakfinancial.com</span>
  </a>

  <span class="offer-text offer-supreme">SUPREME<br>OFFER</span>
  <span class="offer-text offer-think">YOU <span class="small">THINK</span><br><span class="small">&nbsp;&nbsp;&nbsp;&nbsp;&nbsp;&nbsp;&nbsp;&nbsp;WE GIVE</span></span>
  <span class="offer-text offer-start">GET STARTED NOW</span>

  <p class="no-credit"><span class="line-1">NO CREDIT</span><span class="line-2">SCORE</span></p>
</div>
</body>
</html>
```